Professional Business Card for Luxury Hotel & Resort Development Firm. Advisory firm

Project Overview: We are a specialized advisory firm focused on Hotel & Resort Development. Our clients are high-net-worth investors and major hospitality brands.

Design Requirements:

Style: Minimalist, sophisticated, and trustworthy. We want to avoid looking too "corporate" or "dry"—it should feel premium.

Key Elements: Please incorporate our logo [もしロゴがあれば] and emphasize a clean layout with plenty of white space.

Color Palette: We prefer Grey and White or Black and White to evoke a sense of luxury and stability.

Typography: Professional garamond, or sans-serif or elegant serif fonts

Goal: The card should feel substantial and high-end when handed to a client, reflecting our expertise in multi-million dollar developments.
Updates

I am currently on a business trip for field research and have limited access to my desktop. Additionally, I have just provided detailed technical feedback to a designer and am waiting for their refined proposals. To ensure the final logo meets the high standards of my new advisory firm, I would like to extend the deadline by 7 days. Thank you for your support.

Target Market(s)

High-net-worth investors, luxury hospitality brands, and real estate developers.

Contact Information for Business Card

Firm Name: Harbor Crest Partners, My Name: Kenji Morisawa, Title: Founder, Address 5-8-4 Kitanomura Aoba Yokohama Japan 225-0143, email address: kmorisawa@harborcrestpx.example, Tel: +81 90-4183-2750. Front Site (Primary): Japanese translation of the back side, Please use a clean Japanese font (like Mincho) that complements the Garmond on the English side Back side: English. Note for Japanese text: since the frond side is the main fae, please ensure the layout is clean and professional. Please use a high-quality Mincho ( Serif-style) font for Japanese to mach the Garmond used on the English side. Text for Front side (Japanese) Harbor Crest Partners, 役職:代表、森沢健二、225-0143 横浜市青葉区北野村5-8-4. Name of the firm can stay in English.

Font styles to use
Other font styles liked:
• Font Preference: Please use Garamond for all text to maintain a consistent, elegant, and classic professional look.

Requirements
Must have
• Professional and clean layout, high-end feel.
Nice to have
• Minimalist design with subtle luxury accents.

```html
<!DOCTYPE html>
<html lang="ja">
<head>
<meta charset="utf-8">
<title>Harbor Crest Partners — Business Card</title>
<link rel="stylesheet" href="https://fonts.googleapis.com/css2?family=Tinos:ital,wght@0,400;1,400&family=Noto+Sans+JP:wght@400&display=swap">
<style>
  :root {
    --page: #ffffff;
    --card-light: #e9eaea;
    --card-dark: #000000;
    --ink-dark: #111111;
    --ink-light: #ffffff;
    --rule-light: #444444;
    --rule-dark: #bbbbbb;
    --shadow: rgba(0, 0, 0, 0.45);
    --serif: "Tinos", "Times New Roman", serif;
    --jp: "Noto Sans JP", sans-serif;
  }
  * { margin: 0; padding: 0; box-sizing: border-box; }
  html, body {
    width: 1200px;
    height: 1200px;
    overflow: hidden;
    background: var(--page);
  }
  .canvas {
    position: relative;
    width: 1200px;
    height: 1200px;
  }
  .card {
    position: absolute;
    left: 166px;
    width: 857px;
    box-shadow: 4px 4px 6px var(--shadow);
  }
  .card--front {
    top: 117px;
    height: 489px;
    background: var(--card-light);
    color: var(--ink-dark);
  }
  .card--back {
    top: 629px;
    height: 460px;
    background: var(--card-dark);
    color: var(--ink-light);
  }
  .line {
    position: absolute;
    left: 0;
    right: 0;
    text-align: center;
    white-space: nowrap;
    font-family: var(--serif);
  }
  .firm-name {
    font-size: 33px;
    line-height: 40px;
    letter-spacing: 0.09em;
  }
  .card--front .firm-name { top: 126px; }
  .card--back .firm-name { top: 111px; }

  .person-jp {
    top: 206px;
    font-family: var(--jp);
    font-size: 48px;
    line-height: 60px;
    letter-spacing: 0.04em;
  }
  .person-en {
    top: 180px;
    font-size: 38px;
    line-height: 44px;
    letter-spacing: 0.08em;
  }
  .role {
    top: 228px;
    font-style: italic;
    font-size: 25px;
    line-height: 32px;
    letter-spacing: 0.08em;
  }
  .rule {
    position: absolute;
    height: 1px;
  }
  .card--front .rule {
    top: 314px;
    left: 130px;
    width: 600px;
    background: var(--rule-light);
  }
  .card--back .rule {
    top: 285px;
    left: 70px;
    width: 738px;
    background: var(--rule-dark);
  }
  .address-jp {
    top: 340px;
    font-size: 26px;
    line-height: 36px;
    letter-spacing: 0.06em;
  }
  .address-jp .num { font-style: italic; }
  .address-jp .kanji { font-family: var(--jp); letter-spacing: 0.02em; }
  .address-en {
    top: 303px;
    font-size: 21px;
    line-height: 28px;
    letter-spacing: 0.09em;
  }
  .email {
    font-size: 24px;
    line-height: 30px;
    letter-spacing: 0.1em;
  }
  .card--front .email { top: 382px; }
  .card--back .email { top: 347px; }
  .phone {
    font-size: 24px;
    line-height: 30px;
    letter-spacing: 0.1em;
  }
  .card--front .phone { top: 421px; }
  .card--back .phone { top: 387px; }
</style>
</head>
<body>
  <main class="canvas">
    <section class="card card--front" lang="ja">
      <p class="line firm-name">HARBOR CREST PARTNERS</p>
      <h1 class="line person-jp">森沢健二</h1>
      <div class="rule"></div>
      <p class="line address-jp"><span class="num">225-0143</span> <span class="kanji">横浜市青葉区北野村</span><span class="num">5-8-4</span></p>
      <p class="line email">kmorisawa@harborcrestpx.example</p>
      <p class="line phone">+81 90-4183-2750</p>
    </section>

    <section class="card card--back" lang="en">
      <p class="line firm-name">HARBOR CREST PARTNERS</p>
      <h2 class="line person-en">Kenji Morisawa</h2>
      <p class="line role">Founder</p>
      <div class="rule"></div>
      <p class="line address-en">5-8-4 Kitanomura, Aoba, Yokohama Japan 225-0143</p>
      <p class="line email">kmorisawa@harborcrestpx.example</p>
      <p class="line phone">+81 90-4183-2750</p>
    </section>
  </main>
</body>
</html>
```